Tidewell Homecare

I am looking to have a website designed for a housekeeping company that looks similar to this one. https://marlowsnestcare.example/

I need 5 websites designed but will start with this one to see how I like it.

Industry/Entity Type

House Cleaning

Coding

Coded - Design and coding required

Number of Pages Required

5+ page

Font styles to use
Serif
Script

Colors
ffffff
fdf9cf
fbf289
fbee3f
d6edf3
86cae7
33a6d7
edf1f8
cedeed

```html
<!DOCTYPE html>
<html lang="en">
<head>
<meta charset="utf-8">
<title>Tidewell Homecare</title>
<link href="https://fonts.googleapis.com/css2?family=Montserrat:wght@400;500;700&family=Pathway+Gothic+One&display=swap" rel="stylesheet">
<style>
:root{
  --blue:#33a6d7;
  --blue-soft:#86cae7;
  --sky:#d6edf3;
  --yellow:#fbf289;
  --cream:#fdf9cf;
  --line:#cedeed;
  --white:#ffffff;
  --ink:#222831;
  --muted:#5d6470;
}
*{box-sizing:border-box;margin:0;padding:0}
html,body{width:1200px;height:2894px;overflow:hidden;background:var(--white)}
body{position:relative;font-family:'Montserrat',sans-serif;color:var(--ink)}
.abs{position:absolute}
.heading{font-family:'Pathway Gothic One',sans-serif;font-weight:400;color:var(--ink)}
.body-text{font-size:11px;line-height:19px;color:var(--muted)}

/* header */
.site-header{left:0;top:0;width:1200px;height:77px;background:var(--white)}
.brand{left:187px;top:16px;font-weight:700;font-size:31px;line-height:30px;color:var(--blue);letter-spacing:-.5px}
.brand small{display:block;font-size:15px;line-height:16px;font-weight:500;color:var(--muted);letter-spacing:.3px}
.nav{left:535px;top:32px;display:flex;gap:22px;font-size:11px;color:var(--ink)}
.btn-outline{left:882px;top:21px;width:130px;height:39px;border:2px solid var(--blue);color:var(--blue);font-size:11px;display:flex;align-items:center;justify-content:center}

/* hero */
.hero-panel{left:0;top:77px;width:870px;height:490px;background:var(--yellow)}
.hero-photo{left:659px;top:145px;width:481px;height:356px;background:linear-gradient(135deg,#efe7da 0%,#d9c7ad 45%,#f4f1ec 70%,#b89a77 100%)}
.hero-title{left:188px;top:203px;font-size:42px;line-height:44px}
.hero-copy{left:188px;top:320px;width:360px}
.scroll-mouse{left:188px;top:430px}

/* services */
.service-card{top:637px;width:298px;height:297px;border:1px solid var(--line);background:var(--white);padding:26px 26px}
.service-card svg{display:block}
.service-card h3{font-size:20px;margin-top:22px;margin-bottom:14px}
.service-card .body-text{width:248px}
.btn-solid{display:inline-flex;align-items:center;justify-content:center;background:var(--blue);color:var(--white);font-size:11px;font-weight:500;height:37px}
.service-card .btn-solid{margin-top:28px;padding:0 24px}

/* team band */
.team-photo{left:0;top:1004px;width:1200px;height:569px;background:linear-gradient(90deg,#e9e3dc 0%,#9ab7d6 25%,#3f6fae 45%,#e6e2df 60%,#4a79b5 78%,#b4583f 100%)}
.team-card{left:190px;top:1193px;width:481px;height:310px;background:var(--yellow);padding:44px 52px}
.team-card h2{font-size:28px;margin-bottom:16px}
.btn-white{display:inline-flex;align-items:center;justify-content:center;margin-top:28px;width:162px;height:37px;background:var(--white);font-size:11px;color:var(--ink)}

/* form */
.section-title{left:0;width:1200px;text-align:center;font-size:30px}
.field{height:38px;border:1px solid #b8bec6;font-size:11px;color:#8b9199;display:flex;align-items:center;justify-content:space-between;padding:0 14px;width:186px}
.btn-submit{left:518px;top:1837px;width:164px;height:37px}

/* vendors */
.vendors-band{left:0;top:1942px;width:1200px;height:347px;background:var(--sky)}
.vendor-tile{top:2069px;width:260px;height:145px}

/* testimonial */
.quote-box{left:475px;top:2366px;width:537px;height:134px;border:1px solid #b8bec6;padding:32px 30px}
.quote-box p{font-size:13px;line-height:22px;color:var(--muted)}
.avatar{left:509px;top:2485px;width:72px;height:72px;border-radius:50%;background:radial-gradient(circle at 50% 45%,#d6c2b0,#8a7a6d);border:3px solid var(--white)}
.arrow-btn{top:2474px;width:44px;height:44px;border-radius:50%;background:var(--white);box-shadow:0 3px 10px rgba(0,0,0,.12);display:flex;align-items:center;justify-content:center}

/* footer */
.site-footer{left:0;top:2628px;width:1200px;height:266px;background:var(--blue);color:var(--white)}
.footer-title{font-family:'Pathway Gothic One',sans-serif;font-size:20px;color:var(--white);top:2672px}
.footer-text{font-size:10.5px;line-height:22px;color:var(--white)}
.contact-row{display:flex;align-items:center;gap:12px;font-size:10.5px;color:var(--white)}
.subscribe{left:767px;top:2720px;width:245px;height:38px;background:var(--white);display:flex;align-items:center;justify-content:space-between;padding:0 14px;font-size:10.5px;color:#8b9199}
</style>
</head>
<body>

<header class="abs site-header">
  <div class="abs brand">Tidewell<small>Homecare</small></div>
  <nav class="abs nav"><span>Services</span><span>Gift Cards</span><span>About</span><span>Contact</span><span>970-555-0142</span></nav>
  <div class="abs btn-outline">Free Estimate</div>
</header>

<section>
  <div class="abs hero-panel"></div>
  <div class="abs hero-photo" role="img" aria-label="Bright clean kitchen with wooden floor and white cabinets"></div>
  <h1 class="abs heading hero-title">The Importance Of Good<br>Housekeeping</h1>
  <p class="abs body-text hero-copy">Lorem Ipsum is simply dummy text of the printing and typesetting industry. Lorem Ipsum has been the industry's standard dummy text ever since the 1500s, when an unknown printer took a galley of type and scrambled it to make</p>
  <svg class="abs scroll-mouse" width="28" height="40" viewBox="0 0 28 40" fill="none" stroke="#33a6d7" stroke-width="2"><rect x="2" y="2" width="24" height="36" rx="12"/><line x1="14" y1="10" x2="14" y2="17"/></svg>
</section>

<section>
  <div class="abs service-card" style="left:286px">
    <svg width="52" height="40" viewBox="0 0 52 40" fill="none" stroke="#33a6d7" stroke-width="1.8"><path d="M10 18v-6a4 4 0 0 1 4-4h24a4 4 0 0 1 4 4v6"/><rect x="4" y="18" width="44" height="12" rx="4"/><line x1="10" y1="30" x2="10" y2="35"/><line x1="42" y1="30" x2="42" y2="35"/><path d="M4 3l2 2M9 1v3M2 8h3"/></svg>
    <h3 class="heading">Residential Cleaning</h3>
    <p class="body-text">Lorem Ipsum is simply dummy text of the printing and typesetting industry. Lorem Ipsum has been the industry's standard dummy text ever since</p>
    <span class="btn-solid">Residencial Services</span>
  </div>
  <div class="abs service-card" style="left:616px">
    <svg width="52" height="40" viewBox="0 0 52 40" fill="none" stroke="#33a6d7" stroke-width="1.8"><rect x="8" y="8" width="38" height="24" rx="2"/><line x1="27" y1="32" x2="27" y2="37"/><line x1="19" y1="37" x2="35" y2="37"/><path d="M4 3l2 2M9 1v3M2 8h3"/></svg>
    <h3 class="heading">Commercial/Office Cleaning</h3>
    <p class="body-text">Lorem Ipsum is simply dummy text of the printing and typesetting industry. Lorem Ipsum has been the industry's standard dummy text ever since</p>
    <span class="btn-solid">Commercial Services</span>
  </div>
</section>

<section>
  <div class="abs team-photo" role="img" aria-label="Smiling cleaning team in blue overalls with mops and vacuum"></div>
  <div class="abs team-card">
    <h2 class="heading">Hard Work &amp; Reliability</h2>
    <p class="body-text">Lorem Ipsum is simply dummy text of the printing and typesetting industry. Lorem Ipsum has been the industry's standard dummy text ever since the 1500s, when an unknown printer took a galley of type and scrambled it to make a type specimen book. It has survived not only five centuries, but also the leap into electronic typesetting, remaining essentially unchanged.</p>
    <span class="btn-white">Get To Know Us</span>
  </div>
</section>

<section>
  <h2 class="abs heading section-title" style="top:1640px">Free Estimate/Contact Us</h2>
  <div class="abs field" style="left:213px;top:1707px">Name*</div>
  <div class="abs field" style="left:409px;top:1707px">Email*</div>
  <div class="abs field" style="left:605px;top:1707px">City*</div>
  <div class="abs field" style="left:801px;top:1707px">Square Footage*</div>
  <div class="abs field" style="left:213px;top:1760px">Property Type*<span>&#9662;</span></div>
  <div class="abs field" style="left:409px;top:1760px">Type Of Cleaning*<span>&#9662;</span></div>
  <div class="abs field" style="left:605px;top:1760px">Frequency*<span>&#9662;</span></div>
  <div class="abs field" style="left:801px;top:1760px">mm/dd/yyyy<svg width="12" height="12" viewBox="0 0 12 12" fill="none" stroke="#8b9199"><rect x="1" y="2" width="10" height="9"/><line x1="1" y1="5" x2="11" y2="5"/></svg></div>
  <div class="abs btn-solid btn-submit">Submit</div>
</section>

<section>
  <div class="abs vendors-band"></div>
  <h2 class="abs heading section-title" style="top:1998px">Preferred Vendors</h2>
  <div class="abs vendor-tile" style="left:187px;background:linear-gradient(135deg,#4b4f4a,#2b2e2c)" role="img" aria-label="Ridgeline Stays partner tile"></div>
  <div class="abs vendor-tile" style="left:469px;background:linear-gradient(135deg,#6a6560,#4a4541)" role="img" aria-label="Brightfold Restoration partner tile"></div>
  <div class="abs vendor-tile" style="left:752px;background:linear-gradient(135deg,#3a3a3a,#161616)" role="img" aria-label="Pinecrest Linen Co. partner tile"></div>
</section>

<section>
  <h2 class="abs heading" style="left:194px;top:2362px;font-size:30px;line-height:34px">Wwhat Client Say About<br>Us</h2>
  <div class="abs arrow-btn" style="left:196px"><svg width="16" height="10" fill="none" stroke="#33a6d7" stroke-width="1.5"><path d="M15 5H2M6 1L2 5l4 4"/></svg></div>
  <div class="abs arrow-btn" style="left:251px"><svg width="16" height="10" fill="none" stroke="#33a6d7" stroke-width="1.5"><path d="M1 5h13M10 1l4 4-4 4"/></svg></div>
  <div class="abs quote-box"><p>Lorem Ipsum is simply dummy text of the printing and typesetting industry. Lorem Ipsum has been the industry's standard dummy text ever since the 1500s,</p></div>
  <div class="abs avatar" role="img" aria-label="Client portrait"></div>
  <div class="abs heading" style="left:599px;top:2512px;font-size:20px">Sam Carver</div>
</section>

<footer class="abs site-footer"></footer>
<div class="abs footer-title" style="left:187px">Quick Links</div>
<div class="abs footer-text" style="left:187px;top:2712px">Services &nbsp;|&nbsp; Gift Cards &nbsp;|&nbsp; About &nbsp;|&nbsp; Contact<br>|&nbsp; Free Estimate &nbsp;|&nbsp; TH LLC Policy</div>
<div class="abs" style="left:187px;top:2768px;width:22px;height:22px;border-radius:50%;background:var(--white)"></div>

<div class="abs footer-title" style="left:488px">Contact</div>
<div class="abs contact-row" style="left:488px;top:2712px"><svg width="14" height="16" fill="none" stroke="#fff" stroke-width="1.4"><path d="M7 15s-5-5-5-9a5 5 0 0 1 10 0c0 4-5 9-5 9z"/><circle cx="7" cy="6" r="2"/></svg>PO Box 118 | lorem ipsum, CO 100000</div>
<div class="abs contact-row" style="left:488px;top:2745px"><svg width="16" height="12" fill="none" stroke="#fff" stroke-width="1.4"><rect x="1" y="1" width="14" height="10"/><path d="M1 1l7 6 7-6"/></svg>info@tidewellhomecare.example</div>
<div class="abs contact-row" style="left:488px;top:2778px"><svg width="14" height="14" fill="none" stroke="#fff" stroke-width="1.4"><path d="M3 1l3 3-2 2a8 8 0 0 0 4 4l2-2 3 3-2 2C6 13 1 8 1 3z"/></svg>945-555-0187</div>

<div class="abs footer-title" style="left:767px">Newsletter Susbscription</div>
<div class="abs subscribe">Email Address<svg width="18" height="16" viewBox="0 0 18 16" fill="#33a6d7"><path d="M1 8L17 1l-4 14-4-5z"/></svg></div>
<div class="abs footer-text" style="left:767px;top:2774px">© Copyright 2020 Tidewell Homecare</div>

</body>
</html>
```